Current state of Man's Soul Christian view

I would like an improvement of my design or a reimagining of my design to help people visualize what happens to the soul after we die. The second picture "screenshot 2023" is not my design but gives another idea.

For further information, there are 4 "time" frames that could be sectioned off. Eden is one time. Then adam rebellion and pre messiah earth (with hades/ Sheol). The third time frame is Jesus death, resurrection with the current state of earth. The 4th time frame is the "heavenly realm" which is across all 3 times and is unchanged.

For color ideas, please see my website www.brightlanternpath.org which has my color theme. But the death of Jesus I would like in some type of red as well as the death of believers.

My goal is something simple, engaging, and easy to understand. If you have any questions please lmk.
Thank you for considering my project.

```html
<!DOCTYPE html>
<html lang="en">
<head>
<meta charset="utf-8">
<title>What happens to your soul, after you die?</title>
<link href="https://fonts.googleapis.com/css2?family=Poppins:wght@400;500;600;700;800&display=swap" rel="stylesheet">
<style>
  :root {
    --page: #f4f4f2;
    --sky-top: #b9ccd6;
    --sky-mid: #8fd3d8;
    --sky-low: #4cc6cc;
    --teal: #0f7f7e;
    --teal-edge: #c9eeee;
    --ink: #141414;
    --accent-red: #c43a10;
    --death-red: #b5321b;
    --path-dark: #2b1d1a;
    --bar-slate: #3b3a48;
    --bar-gold: #b88a3c;
    --white: #ffffff;
  }
  html, body {
    margin: 0;
    padding: 0;
    width: 822px;
    height: 1200px;
    overflow: hidden;
    background: var(--page);
    font-family: "Poppins", sans-serif;
  }
  .canvas { position: relative; width: 822px; height: 1200px; }
  .poster {
    position: absolute;
    left: 21px;
    top: 324px;
    width: 780px;
    height: 552px;
    box-shadow: 0 6px 18px rgba(0,0,0,0.22);
  }
  .poster svg { display: block; }
  .box-label { fill: var(--white); font-weight: 600; text-anchor: middle; }
  .title-line { fill: var(--ink); font-weight: 500; font-size: 30px; }
  .title-accent { fill: var(--accent-red); font-weight: 800; font-size: 30px; }
  .stack { fill: var(--white); font-weight: 700; text-anchor: middle; }
  .stack-dark { fill: var(--ink); }
  .realm-label { fill: var(--white); font-weight: 600; font-size: 13px; text-anchor: middle; }
  .brand { fill: var(--white); font-weight: 500; font-size: 17px; }
</style>
</head>
<body>
<main class="canvas">
  <section class="poster">
    <svg width="780" height="552" viewBox="0 0 780 552" xmlns="http://www.w3.org/2000/svg">
      <defs>
        <linearGradient id="sky" x1="0" y1="0" x2="0" y2="1">
          <stop offset="0" stop-color="var(--sky-top)"/>
          <stop offset="0.45" stop-color="var(--sky-mid)"/>
          <stop offset="1" stop-color="var(--sky-low)"/>
        </linearGradient>
        <radialGradient id="eden" cx="0.5" cy="0.45" r="0.6">
          <stop offset="0" stop-color="#fbfbe0"/>
          <stop offset="0.55" stop-color="#a8dd7a"/>
          <stop offset="1" stop-color="#4f9c3a"/>
        </radialGradient>
        <radialGradient id="fallen" cx="0.4" cy="0.35" r="0.7">
          <stop offset="0" stop-color="#4b5a6e"/>
          <stop offset="0.6" stop-color="#1d2230"/>
          <stop offset="1" stop-color="#7a2d10"/>
        </radialGradient>
        <radialGradient id="earth" cx="0.45" cy="0.4" r="0.65">
          <stop offset="0" stop-color="#e6dcc0"/>
          <stop offset="0.45" stop-color="#6c9a58"/>
          <stop offset="1" stop-color="#1f4f7e"/>
        </radialGradient>
        <linearGradient id="hades" x1="0" y1="0" x2="0" y2="1">
          <stop offset="0" stop-color="#6b6a6e"/>
          <stop offset="0.3" stop-color="#e7c69a"/>
          <stop offset="0.55" stop-color="#7a4a32"/>
          <stop offset="0.8" stop-color="#b8361a"/>
          <stop offset="1" stop-color="#3a120a"/>
        </linearGradient>
        <linearGradient id="risen" x1="0" y1="0" x2="0" y2="1">
          <stop offset="0" stop-color="#f3e9da"/>
          <stop offset="0.5" stop-color="#3f62a8"/>
          <stop offset="1" stop-color="#e9ddd0"/>
        </linearGradient>
        <linearGradient id="jesusDeath" x1="0" y1="0" x2="0" y2="1">
          <stop offset="0" stop-color="var(--path-dark)"/>
          <stop offset="1" stop-color="var(--bar-gold)"/>
        </linearGradient>
      </defs>

      <!-- sky backdrop -->
      <rect width="780" height="552" fill="url(#sky)" role="img" aria-label="Sky of clouds with distant heavenly city spires"/>

      <!-- title -->
      <text class="title-line" x="40" y="60">What happens</text>
      <text class="title-line" x="40" y="88">to your soul,</text>
      <text class="title-accent" x="40" y="118">After you die?</text>

      <!-- heaven box -->
      <rect x="327" y="51" width="236" height="43" rx="4" fill="var(--teal)" stroke="var(--teal-edge)" stroke-width="1.5"/>
      <text class="box-label" x="445" y="70" font-size="15">3<tspan font-size="8" dy="-6">RD</tspan><tspan dy="6"> HEAVEN</tspan></text>
      <text class="box-label" x="445" y="88" font-size="14.5">GOD'S HEAVENLY THRONE</text>

      <!-- era labels -->
      <rect x="268" y="105" width="121" height="44" rx="4" fill="var(--teal)" stroke="var(--teal-edge)" stroke-width="1.5"/>
      <text class="box-label" x="328" y="124" font-size="13.5">PRE-MESSIAH</text>
      <text class="box-label" x="328" y="141" font-size="13.5">FALLEN EARTH</text>

      <rect x="536" y="105" width="122" height="44" rx="4" fill="var(--teal)" stroke="var(--teal-edge)" stroke-width="1.5"/>
      <text class="box-label" x="597" y="124" font-size="13.5">CURRENT</text>
      <text class="box-label" x="597" y="141" font-size="13.5">FALLEN EARTH</text>

      <rect x="73" y="203" width="78" height="34" rx="4" fill="var(--teal)" stroke="var(--teal-edge)" stroke-width="1.5"/>
      <text class="box-label" x="112" y="227" font-size="19">EDEN</text>

      <rect x="160" y="204" width="85" height="33" rx="4" fill="var(--teal)" stroke="var(--teal-edge)" stroke-width="1.5"/>
      <circle cx="165" cy="221" r="9" fill="#c6202a"/>
      <text class="box-label" x="208" y="219" font-size="10">ADAM</text>
      <text class="box-label" x="208" y="231" font-size="10">REBELLION</text>

      <!-- Eden -->
      <circle cx="112" cy="319" r="74" fill="url(#eden)" stroke="var(--teal)" stroke-width="3" role="img" aria-label="Garden of Eden with Adam and Eve among trees"/>

      <!-- death path -->
      <path d="M209 360 V446 H356" fill="none" stroke="var(--path-dark)" stroke-width="20"/>
      <polygon points="352,434 368,446 352,458" fill="var(--path-dark)"/>
      <rect x="189" y="248" width="39" height="120" rx="5" fill="var(--death-red)"/>
      <text class="stack" x="209" font-size="22">
        <tspan x="209" y="272">D</tspan><tspan x="209" dy="22">E</tspan><tspan x="209" dy="22">A</tspan><tspan x="209" dy="22">T</tspan><tspan x="209" dy="22">H</tspan>
      </text>
      <text x="222" y="451" fill="var(--white)" font-size="8" font-weight="600">WIDE GATE</text>

      <!-- narrow gate -->
      <text x="234" y="319" fill="var(--white)" font-size="7" font-weight="600">NARROW</text>
      <path d="M237 322 H260 V344" fill="none" stroke="var(--ink)" stroke-width="1.5"/>
      <polygon points="255,342 265,342 260,352" fill="var(--ink)"/>
      <text class="stack stack-dark" font-size="5.5">
        <tspan x="266" y="330">G</tspan><tspan x="266" dy="6">A</tspan><tspan x="266" dy="6">T</tspan><tspan x="266" dy="6">E</tspan>
      </text>

      <!-- pre-messiah earth -->
      <circle cx="330" cy="233" r="76" fill="url(#fallen)" stroke="var(--teal)" stroke-width="3" role="img" aria-label="Dark fallen earth with fires"/>

      <!-- left hades -->
      <circle cx="330" cy="403" r="78" fill="url(#hades)" stroke="var(--teal)" stroke-width="3" role="img" aria-label="Hades divided into cloudy paradise above and fiery torment below"/>
      <line x1="254" y1="408" x2="406" y2="408" stroke="#5fc7c4" stroke-width="1.5"/>
      <text class="realm-label" x="330" y="397">PARADISE</text>
      <text class="realm-label" x="330" y="428">TORMENT</text>
      <rect x="282" y="492" width="91" height="31" rx="4" fill="var(--teal)" stroke="var(--teal-edge)" stroke-width="1.5"/>
      <text class="box-label" x="327" y="512" font-size="10.5">HADES/SHEOL</text>

      <!-- Jesus death -->
      <rect x="405" y="162" width="48" height="5" fill="var(--path-dark)"/>
      <rect x="420" y="155" width="19" height="214" fill="url(#jesusDeath)"/>
      <path d="M439 360 H400" stroke="var(--path-dark)" stroke-width="12"/>
      <polygon points="404,350 388,360 404,370" fill="var(--path-dark)"/>
      <text class="stack stack-dark" font-size="11.5">
        <tspan x="429.5" y="180">J</tspan><tspan x="429.5" dy="13">E</tspan><tspan x="429.5" dy="13">S</tspan><tspan x="429.5" dy="13">U</tspan><tspan x="429.5" dy="13">S</tspan><tspan x="429.5" dy="26">D</tspan><tspan x="429.5" dy="13">E</tspan><tspan x="429.5" dy="13">A</tspan><tspan x="429.5" dy="13">T</tspan><tspan x="429.5" dy="13">H</tspan>
      </text>

      <!-- ascension -->
      <polygon points="478,108 498,140 458,140" fill="#5f6a78"/>
      <rect x="464" y="138" width="28" height="24" fill="#5f6a78"/>
      <rect x="464" y="245" width="18" height="167" fill="#6a6f7e"/>
      <text class="stack" font-size="7.5">
        <tspan x="473" y="258">J</tspan><tspan x="473" dy="8.6">E</tspan><tspan x="473" dy="8.6">S</tspan><tspan x="473" dy="8.6">U</tspan><tspan x="473" dy="8.6">S</tspan><tspan x="473" dy="12">R</tspan><tspan x="473" dy="8.6">E</tspan><tspan x="473" dy="8.6">S</tspan><tspan x="473" dy="8.6">S</tspan><tspan x="473" dy="8.6">U</tspan><tspan x="473" dy="8.6">R</tspan><tspan x="473" dy="8.6">E</tspan><tspan x="473" dy="8.6">C</tspan><tspan x="473" dy="8.6">T</tspan><tspan x="473" dy="8.6">I</tspan><tspan x="473" dy="8.6">O</tspan><tspan x="473" dy="8.6">N</tspan>
      </text>
      <rect x="436" y="142" width="66" height="108" rx="20" fill="url(#risen)" role="img" aria-label="Risen Jesus ascending in robes"/>

      <!-- holy spirit descends -->
      <rect x="501" y="99" width="15" height="155" fill="var(--bar-slate)"/>
      <text class="stack" font-size="6.4">
        <tspan x="508.5" y="108">H</tspan><tspan x="508.5" dy="7.3">O</tspan><tspan x="508.5" dy="7.3">L</tspan><tspan x="508.5" dy="7.3">Y</tspan><tspan x="508.5" dy="7.3">S</tspan><tspan x="508.5" dy="7.3">P</tspan><tspan x="508.5" dy="7.3">I</tspan><tspan x="508.5" dy="7.3">R</tspan><tspan x="508.5" dy="7.3">I</tspan><tspan x="508.5" dy="7.3">T</tspan><tspan x="508.5" dy="11">D</tspan><tspan x="508.5" dy="7.3">E</tspan><tspan x="508.5" dy="7.3">S</tspan><tspan x="508.5" dy="7.3">C</tspan><tspan x="508.5" dy="7.3">E</tspan><tspan x="508.5" dy="7.3">N</tspan><tspan x="508.5" dy="7.3">D</tspan><tspan x="508.5" dy="7.3">S</tspan>
      </text>
      <path d="M508 250 H540" stroke="var(--path-dark)" stroke-width="8"/>
      <polygon points="538,242 552,250 538,258" fill="var(--path-dark)"/>

      <!-- current earth -->
      <circle cx="602" cy="233" r="79" fill="url(#earth)" stroke="var(--teal)" stroke-width="3" role="img" aria-label="Earth seen from space"/>

      <!-- believers in Jesus -->
      <rect x="603" y="70" width="118" height="24" fill="var(--path-dark)"/>
      <polygon points="606,58 584,82 606,106" fill="var(--path-dark)"/>
      <rect x="693" y="65" width="28" height="223" fill="var(--bar-slate)"/>
      <text class="stack" font-size="11.5">
        <tspan x="707" y="82">B</tspan><tspan x="707" dy="12">E</tspan><tspan x="707" dy="12">L</tspan><tspan x="707" dy="12">I</tspan><tspan x="707" dy="12">E</tspan><tspan x="707" dy="12">V</tspan><tspan x="707" dy="12">E</tspan><tspan x="707" dy="12">R</tspan><tspan x="707" dy="12">S</tspan><tspan x="707" dy="20">I</tspan><tspan x="707" dy="12">N</tspan><tspan x="707" dy="20">J</tspan><tspan x="707" dy="12">E</tspan><tspan x="707" dy="12">S</tspan><tspan x="707" dy="12">U</tspan><tspan x="707" dy="12">S</tspan>
      </text>
      <rect x="661" y="296" width="82" height="26" rx="3" fill="var(--death-red)" stroke="var(--teal-edge)" stroke-width="1"/>
      <text class="box-label" x="702" y="314" font-size="12.5">AT DEATH</text>

      <!-- right hades -->
      <circle cx="598" cy="406" r="78" fill="url(#hades)" stroke="var(--teal)" stroke-width="3" role="img" aria-label="Hades divided into cloudy paradise above and fiery torment below"/>
      <line x1="522" y1="411" x2="674" y2="411" stroke="#5fc7c4" stroke-width="1.5"/>
      <text class="realm-label" x="598" y="400">PARADISE</text>
      <text class="realm-label" x="598" y="430">TORMENT</text>
      <rect x="552" y="492" width="92" height="31" rx="4" fill="var(--teal)" stroke="var(--teal-edge)" stroke-width="1.5"/>
      <text class="box-label" x="598" y="512" font-size="10.5">HADES/SHEOL</text>

      <!-- non believers -->
      <path d="M706 444 H664" stroke="var(--ink)" stroke-width="9"/>
      <polygon points="668,432 652,444 668,456" fill="var(--ink)"/>
      <rect x="699" y="338" width="14" height="112" fill="var(--ink)"/>
      <text class="stack" font-size="7.5">
        <tspan x="706" y="348">N</tspan><tspan x="706" dy="8">O</tspan><tspan x="706" dy="8">N</tspan><tspan x="706" dy="12">B</tspan><tspan x="706" dy="8">E</tspan><tspan x="706" dy="8">L</tspan><tspan x="706" dy="8">I</tspan><tspan x="706" dy="8">E</tspan><tspan x="706" dy="8">V</tspan><tspan x="706" dy="8">E</tspan><tspan x="706" dy="8">R</tspan><tspan x="706" dy="8">S</tspan>
      </text>

      <!-- brand -->
      <circle cx="55" cy="494" r="9" fill="var(--white)"/>
      <text class="brand" x="72" y="500">Bright Lantern Path</text>
    </svg>
  </section>
</main>
</body>
</html>
```